wardrobe/costume stylist needs good business card for own business

Hi:)

I'm wanting a business card for my company. I am a freelance stylist.

I do wardrobe/costume stylist to TV commercials; Films; Fashion and Lifestyle shoots.

I'd like a design based around my name Rosalind Pember written nicely, maybe a colour? Up to you?!

I've attached a couple of images of business cards I like
.... be creative and have fun!

Thank you :)
Updates

Reason: I was trying to get my new business card ready for before I headed overseas Friday morning but I don't think that was realistic so I'd like to extend the deadline to give time to the project. Thank you

Hi designers:) Thank you for all your designs, I've extended the deadline until Sunday, so there's a bit more time. I've attached 3 pictures of business cards which I quite like, please take a look to see if it can be of help in your process. I like the pale plain or patterned background with dark font and the dark plain or patterned background with the pale font the motifs the feminine fonts the plain fonts I like the idea of playing with a circle or some shape on one side of the card with my name or initials as in the picture I have on my post could you play around with this idea a bit please? Thank you all for the work you've done :) Rosa

Hi I am working overseas til Saturday night sorry for no feedback until I teturn Thanks :) Rosa

Hi designers, Thank you all so much for submitting your designs, I really appreciate your input into my project :) I'm sorry I didn't get to respond to some comments, and give feedback. I didn't back from being away until later than I expected, and the deadline had passed then, so apologies. Thanks to you all again for all your really good designs :) Rosa

Target Market(s)

I am a freelance stylist my target audience is producers, production companies, photographers, directors...

Industry/Entity Type

Business

Requirements
Must have
• Rosalind Pember
Stylist or Wardrobe Stylist

email rosapember@quillnet.co.nz
Mobile 0218846193

(Don't have to use the words 'email' and 'mobile')
Nice to have
• Would like it to be double sided
Like B & W
Like pale colour background with dark font or white font
Like dark colour background with pale font
Should not have
• I would prefer it not to incorporate pictures

```html
<!DOCTYPE html>
<html lang="en">
<head>
<meta charset="utf-8">
<title>Rosalind Pember — Stylist business cards</title>
<link rel="stylesheet" href="https://fonts.googleapis.com/css2?family=Poiret+One&family=Josefin+Sans:wght@300;400&display=swap">
<style>
  :root {
    --backdrop: #2b2e31;
    --card-dark: #141517;
    --card-sage: #b3b38d;
    --ink-pale: #d9d5b2;
    --ink-dark: #1a1a18;
    --ornament-on-dark: #8f8c72;
    --ornament-on-sage: #6f6e55;
  }
  * { margin: 0; padding: 0; box-sizing: border-box; }
  html, body {
    width: 1200px; height: 1000px; overflow: hidden;
    background: var(--backdrop);
  }
  .sheet {
    position: relative; width: 1200px; height: 1000px;
  }
  .card {
    position: absolute; width: 500px; height: 290px;
    overflow: hidden;
    box-shadow: 0 10px 24px rgba(0,0,0,.35);
  }
  .card--dark { background: var(--card-dark); color: var(--ink-pale); }
  .card--sage { background: var(--card-sage); color: var(--ink-dark); }

  .card--front-dark { left: 70px;  top: 150px; }
  .card--front-sage { left: 630px; top: 150px; }
  .card--back-sage  { left: 70px;  top: 560px; }
  .card--back-dark  { left: 630px; top: 560px; }

  .name {
    position: absolute;
    font-family: "Poiret One", sans-serif;
    font-weight: 400;
    white-space: nowrap;
    letter-spacing: 0.5px;
  }
  .front .name { left: 40px; top: 118px; font-size: 60px; }
  .back  .name { left: 62px; top: 42px;  font-size: 44px; }

  .ornament { position: absolute; border-radius: 40% 60% 45% 55%; }
  .card--dark .ornament {
    background: radial-gradient(ellipse at center, var(--ornament-on-dark) 0%, rgba(143,140,114,.35) 60%, rgba(143,140,114,0) 100%);
  }
  .card--sage .ornament {
    background: radial-gradient(ellipse at center, var(--ornament-on-sage) 0%, rgba(111,110,85,.35) 60%, rgba(111,110,85,0) 100%);
  }
  .front .ornament--crown  { left: 48px;  top: 34px;  width: 150px; height: 90px; }
  .front .ornament--tail   { left: 420px; top: 200px; width: 70px;  height: 46px; }
  .back  .ornament--corner { left: 16px;  top: 14px;  width: 90px;  height: 56px; }
  .back  .ornament--foot   { left: 398px; top: 184px; width: 82px;  height: 62px; }

  .rule { position: absolute; height: 1px; }
  .card--dark .rule { background: var(--ink-pale); }
  .card--sage .rule { background: var(--ink-dark); }
  .rule--top    { left: 18px;  top: 104px; width: 300px; }
  .rule--bottom { left: 270px; top: 252px; width: 214px; }

  .role {
    position: absolute; left: 290px; top: 112px;
    font-family: "Josefin Sans", sans-serif; font-weight: 300; font-size: 17px;
  }
  .contact {
    position: absolute; left: 34px; top: 164px;
    font-family: "Josefin Sans", sans-serif; font-weight: 300;
    font-size: 18px; line-height: 34px; list-style: none;
  }
  .contact .phone { font-size: 22px; letter-spacing: 1px; }
</style>
</head>
<body>
<main class="sheet">

  <section class="card card--dark front card--front-dark">
    <div class="ornament ornament--crown" role="img" aria-label="Baroque scroll flourish"></div>
    <h1 class="name">Rosalind Pember</h1>
    <div class="ornament ornament--tail" role="img" aria-label="Small baroque scroll flourish"></div>
  </section>

  <section class="card card--sage front card--front-sage">
    <div class="ornament ornament--crown" role="img" aria-label="Baroque scroll flourish"></div>
    <h1 class="name">Rosalind Pember</h1>
    <div class="ornament ornament--tail" role="img" aria-label="Small baroque scroll flourish"></div>
  </section>

  <section class="card card--sage back card--back-sage">
    <div class="ornament ornament--corner" role="img" aria-label="Baroque scroll flourish"></div>
    <div class="rule rule--top"></div>
    <h2 class="name">Rosalind Pember</h2>
    <p class="role">Stylist</p>
    <ul class="contact">
      <li class="email">rosapember@quillnet.co.nz</li>
      <li class="phone">021 884 6193</li>
    </ul>
    <div class="ornament ornament--foot" role="img" aria-label="Baroque scroll flourish"></div>
    <div class="rule rule--bottom"></div>
  </section>

  <section class="card card--dark back card--back-dark">
    <div class="ornament ornament--corner" role="img" aria-label="Baroque scroll flourish"></div>
    <div class="rule rule--top"></div>
    <h2 class="name">Rosalind Pember</h2>
    <p class="role">Stylist</p>
    <ul class="contact">
      <li class="email">rosapember@quillnet.co.nz</li>
      <li class="phone">021 884 6193</li>
    </ul>
    <div class="ornament ornament--foot" role="img" aria-label="Baroque scroll flourish"></div>
    <div class="rule rule--bottom"></div>
  </section>

</main>
</body>
</html>
```